Postcard Design

Baxley is a Orbit Cab and hire car service that specializes in airport to hotel transfers and surrounding suburbs at affordable rates . we offer a personalize service with over 40 years industry experience. we would like to promote a special from melbourne cbd to airport for $65 , our contact number is 0481926370, email primecabride@brisolmail.com , orbit cab and hire car services we plan on distributing these flyers at all major hotels

Industry/Entity Type

Hotel

```html
<!DOCTYPE html>
<html lang="en">
<head>
<meta charset="utf-8">
<title>Baxley Orbit Cab – Postcard</title>
<link rel="stylesheet" href="https://fonts.googleapis.com/css2?family=Anton&family=Oswald:wght@500;700&family=Open+Sans:wght@400;600&family=Fira+Sans+Condensed:wght@400;600;700&family=Dancing+Script:wght@600&display=swap">
<style>
  :root {
    --backdrop: #2b2019;
    --red: #e21c23;
    --blue: #1f56b3;
    --blue-deep: #1e3f9b;
    --blue-card: #2d4ea6;
    --paper: #f1f2f3;
    --grey: #e6e7e9;
    --ink: #1b1b1b;
    --white: #ffffff;
    --gold: #f7cf1d;
    --photo-sky: #d9dde0;
    --photo-dark: #2f3338;
  }
  * { margin: 0; padding: 0; box-sizing: border-box; }
  html, body { width: 863px; height: 1200px; overflow: hidden; }
  body { background: var(--backdrop); position: relative; font-family: "Open Sans", sans-serif; }

  /* Front of postcard */
  .card-front {
    position: absolute; left: 114px; top: 60px; width: 671px; height: 518px;
    background: var(--paper); overflow: hidden;
  }
  .front-topband { position: absolute; left: 0; top: 0; width: 100%; height: 18px;
    background: linear-gradient(90deg, var(--blue) 0%, var(--blue-deep) 100%); }
  .front-title { position: absolute; left: 35px; top: 22px; font-family: "Oswald", sans-serif; font-weight: 700;
    font-size: 60px; line-height: 1.1; color: var(--red); letter-spacing: 1px; white-space: nowrap; }
  .front-subtitle { position: absolute; left: 35px; top: 104px; font-family: "Oswald", sans-serif;
    font-weight: 700; font-size: 21.5px; line-height: 29px; color: var(--blue); text-transform: uppercase; letter-spacing: .2px; }
  .front-photo { position: absolute; left: 0; top: 193px; width: 100%; height: 325px;
    background: linear-gradient(180deg, var(--photo-sky) 0%, #c4c9cd 45%, #6b7075 70%, var(--photo-dark) 100%); }
  .front-intro { position: absolute; left: 130px; top: 180px; width: 300px; text-align: center;
    font-size: 23px; line-height: 29px; color: var(--ink); }
  .special-box { position: absolute; left: 31px; top: 366px; width: 225px; height: 136px;
    background: var(--red); color: var(--white); font-family: "Fira Sans Condensed", sans-serif;
    font-weight: 700; font-size: 22px; line-height: 27px; text-align: center; padding-top: 10px; }
  .special-box .price { font-size: 31px; }
  .front-bottomband { position: absolute; left: 0; bottom: 0; width: 100%; height: 48px;
    background: linear-gradient(90deg, var(--blue) 0%, var(--blue-deep) 100%);
    clip-path: polygon(0 65%, 56% 65%, 58% 0, 100% 0, 100% 100%, 0 100%); }
  .front-email { position: absolute; right: 30px; top: 440px; font-family: "Fira Sans Condensed", sans-serif;
    font-weight: 600; font-size: 20px; color: var(--white); text-shadow: 0 1px 3px rgba(0,0,0,.6); }
  .front-contact { position: absolute; right: 24px; top: 470px; display: flex; align-items: baseline; gap: 12px; color: var(--white); }
  .contact-label { font-family: "Dancing Script", cursive; font-size: 26px; }
  .contact-number { font-family: "Oswald", sans-serif; font-weight: 700; font-size: 33px; letter-spacing: 1.5px; }

  /* Back of postcard */
  .card-back {
    position: absolute; left: 112px; top: 606px; width: 669px; height: 514px;
    background: var(--blue-card);
  }
  .back-paper { position: absolute; left: 0; top: 12px; right: 8px; bottom: 10px; background: var(--grey); }
  .back-header { position: absolute; left: 0; top: 0; width: 508px; height: 164px;
    background: linear-gradient(135deg, #2a4aa5 0%, #3a62c4 55%, #2846a0 100%); }
  .back-feature { position: absolute; left: 0; top: 164px; width: 325px; height: 264px;
    background: linear-gradient(160deg, #3a62c4 0%, #2846a0 100%); }
  .back-title { position: absolute; left: 32px; top: 20px; font-family: "Anton", sans-serif;
    font-size: 60px; line-height: 1; color: var(--white); letter-spacing: 1px; white-space: nowrap; }
  .back-email { position: absolute; left: 32px; top: 84px; font-size: 19px; color: var(--white); }
  .back-contact { position: absolute; left: 32px; top: 116px; display: flex; align-items: baseline; gap: 10px; color: var(--white); }
  .back-contact .contact-label { font-size: 22px; }
  .back-contact .contact-number { font-size: 30px; }
  .social { position: absolute; left: 333px; top: 122px; display: flex; align-items: center; gap: 8px;
    font-family: "Fira Sans Condensed", sans-serif; font-weight: 400; font-size: 17px; color: var(--white); }
  .social-dot { width: 26px; height: 26px; border-radius: 50%; background: var(--white); opacity: .9; }
  .badge { position: absolute; left: 24px; top: 158px; width: 124px; height: 124px; }
  .badge-text { position: absolute; left: 24px; top: 172px; width: 124px; text-align: center;
    font-family: "Anton", sans-serif; color: var(--ink); line-height: 1; }
  .badge-text .amount { font-size: 30px; display: block; }
  .badge-text .label { font-size: 27px; display: block; }
  .badge-text .route { font-family: "Fira Sans Condensed", sans-serif; font-weight: 700; font-size: 10px; line-height: 12px; display: block; margin-top: 3px; }
  .back-brand { position: absolute; left: 160px; top: 180px; font-family: "Oswald", sans-serif; font-weight: 700;
    font-size: 34px; line-height: 38px; color: var(--red); white-space: nowrap; }
  .car-photo { position: absolute; left: 14px; top: 272px; width: 310px; height: 134px; border-radius: 30px 40px 12px 12px;
    background: linear-gradient(180deg, #6d7175 0%, #45494d 60%, #2a2c2f 100%); }
  .back-tagline { position: absolute; left: 10px; top: 410px; font-family: "Fira Sans Condensed", sans-serif;
    font-weight: 400; font-size: 11px; color: var(--white); white-space: nowrap; }
  .area-label { position: absolute; font-size: 15px; color: var(--ink); transform: translateX(-50%); white-space: nowrap; }
</style>
</head>
<body>

<section class="card-front" aria-label="Postcard front">
  <div class="front-topband"></div>
  <h1 class="front-title">BAXLEY - ORBIT CAB</h1>
  <p class="front-subtitle">Hire car service that specializes in airport to hotel<br>transfers and surrounding suburbs at affordable rates</p>
  <div class="front-photo" role="img" aria-label="Photo of a chauffeur holding an umbrella for a passenger stepping from a black sedan beside a jet on the tarmac"></div>
  <p class="front-intro">We offer a personalize service with over 40 years industry experience.</p>
  <div class="special-box">We would like to<br>promote a SPECIAL<br>from Melbourne cbd<br>to Airport for <span class="price">$65</span></div>
  <div class="front-bottomband"></div>
  <p class="front-email">email: primecabride@brisolmail.com</p>
  <p class="front-contact"><span class="contact-label">Contact Us:</span><span class="contact-number">0481926370</span></p>
</section>

<section class="card-back" aria-label="Postcard back">
  <div class="back-paper"></div>
  <div class="back-header"></div>
  <div class="back-feature"></div>
  <h2 class="back-title">HIRE CAR SERVICES</h2>
  <p class="back-email">email: primecabride@brisolmail.com</p>
  <p class="back-contact"><span class="contact-label">Contact Us:</span><span class="contact-number">0481926370</span></p>
  <p class="social"><span class="social-dot"></span>orbit cab</p>

  <svg class="badge" viewBox="0 0 124 124" aria-hidden="true">
    <circle cx="62" cy="62" r="61" fill="#e21c23"/>
    <circle cx="62" cy="62" r="52" fill="#f7cf1d"/>
  </svg>
  <p class="badge-text"><span class="amount">&amp;65</span><span class="label">SPECIAL</span><span class="route">Melbourne cbd to<br>Airport</span></p>

  <p class="back-brand">BAXLEY<br>ORBIT CAB</p>
  <div class="car-photo" role="img" aria-label="Photo of a grey executive sedan"></div>
  <p class="back-tagline">We offer a personalize service with over 40 years industry experience</p>

  <p class="area-label" style="left:573px; top:84px;">stamp</p>
  <p class="area-label" style="left:508px; top:384px;">Address area</p>
  <p class="area-label" style="left:224px; top:468px;">Barcode area</p>
</section>

</body>
</html>
```